Stationery and business cards - New design

I need following designs
- writing paper for business letters A4, you can take the data from our old paper. There should just be a place for a third bank account.
- writing paper for business letters (only design + logo, without address, bank accounts and legal data)
- business cards with qr code, one side, only German language (you can take the data from the old layout)

Target Market(s)

Industrial customers

Industry/Entity Type

sheet metal technology, laser cutting of metal sheet

Requirements
Must have
• The address above the recipient should be placed like on my old paper. No relationship to the old design (only color) - please make a completely new design.
Nice to have
• colors like in my new logo
Should not have
• - the business letter should be suitable for borderless print - the green timber in my old paper is very bad for this - so please make a design without a timber (or a timber like it is on my old paper)

```html
<!DOCTYPE html>
<html lang="de">
<head>
<meta charset="utf-8">
<title>Tannfeld Blechtechnik – Geschäftsausstattung</title>
<link rel="stylesheet" href="https://fonts.googleapis.com/css2?family=Arimo:wght@400;700&family=PT+Sans:wght@400&display=swap">
<style>
  :root{
    --backdrop:#3a3b3c;
    --paper:#f6f4f5;
    --card:#ffffff;
    --brand-blue:#1f4a8c;
    --brand-teal:#1a8fa7;
    --ink:#2b2b2b;
    --body:#4a4a4a;
    --muted:#666;
    --rule:#1a8fa7;
  }
  *{margin:0;padding:0;box-sizing:border-box}
  html,body{width:1200px;height:989px;overflow:hidden;background:var(--backdrop)}
  .canvas{position:relative;width:1200px;height:989px}

  /* brand name */
  .brand{position:absolute;display:flex;align-items:center;gap:6px}
  .brand-dot{border-radius:50%;background:var(--brand-teal);flex:none}
  .brand-name{font-family:'Arimo',sans-serif;font-weight:700;color:var(--brand-blue);letter-spacing:.5px}

  /* business card */
  .card{position:absolute;left:83px;top:395px;width:351px;height:200px;background:var(--card);border-radius:12px}
  .card .brand{left:22px;top:84px}
  .card .brand-dot{width:30px;height:30px}
  .card .brand-name{font-size:16px}
  .card-divider{position:absolute;left:170px;top:41px;width:1px;height:117px;background:#9aa5ad}
  .card-info{position:absolute;left:183px;top:36px;font-family:'PT Sans',sans-serif;font-weight:400;color:var(--ink)}
  .card-name{font-family:'Arimo',sans-serif;font-weight:700;font-size:15px;color:var(--brand-blue);line-height:18px}
  .card-title{font-family:'Arimo',sans-serif;font-size:8.6px;color:var(--brand-teal);line-height:11.5px;margin-top:2px}
  .card-address{font-size:8.6px;line-height:11px;margin-top:10px}
  .contact-list{list-style:none;margin-top:7px;font-size:8.6px;line-height:11.6px}
  .contact-list li{display:flex;align-items:center;gap:5px}
  .contact-list svg{width:7px;height:7px;fill:var(--brand-blue);flex:none}

  /* letterhead */
  .letter{position:absolute;left:517px;top:85px;width:595px;height:836px;background:var(--paper);overflow:hidden}
  .letter .brand{left:381px;top:41px}
  .letter .brand-dot{width:34px;height:34px}
  .letter .brand-name{font-size:19px}
  .sender-line{position:absolute;left:58px;top:98px;font-size:5.6px;color:var(--muted);font-family:'PT Sans',sans-serif}
  .letter-address{position:absolute;left:382px;top:96px;font-family:'PT Sans',sans-serif;font-weight:400;font-size:8.5px;line-height:10.8px;color:var(--ink)}
  .letter-address .contact-list{margin-top:7px;font-size:8.3px}
  .letter-body{position:absolute;left:60px;top:214px;width:478px;font-family:'Arimo',sans-serif;color:var(--body)}
  .salutation{font-size:16px;color:#444;margin-bottom:30px}
  .letter-body p.text{font-size:9.9px;line-height:14.3px;text-align:justify;margin-bottom:14.3px;hyphens:auto}
  .closing{font-size:10px;margin-top:26px}
  .signature{width:77px;height:24px;margin:12px 0 20px -3px;background:linear-gradient(90deg,transparent,rgba(30,30,30,.25),transparent);border-radius:12px}
  .signer{font-size:13px;color:#333;margin-left:3px}
  .signer-role{font-size:10px;color:#333;margin-left:3px;margin-top:2px}

  .letter-footer{position:absolute;left:45px;top:771px;display:flex;font-family:'PT Sans',sans-serif;font-size:5.5px;line-height:8px;color:#444}
  .footer-col{padding:0 6px;border-left:1px solid var(--rule)}
  .footer-col:first-child{border-left:none;padding-left:0;width:53px}
  .footer-col:nth-child(2){width:117px}
  .footer-col:nth-child(3){width:110px}
  .footer-col:nth-child(4){width:118px}
  .footer-note{position:absolute;left:0;width:100%;top:814px;text-align:center;font-family:'PT Sans',sans-serif;font-size:5.6px;color:#444}
</style>
</head>
<body>
<div class="canvas">

  <svg width="0" height="0" style="position:absolute">
    <symbol id="icon-phone" viewBox="0 0 10 10"><path d="M2 0.5l2 2-1 1.2c.6 1.3 1.5 2.2 2.8 2.8L7 5.5l2 2-1.3 1.8C4 9 1 6 .7 2.3z"/></symbol>
    <symbol id="icon-fax" viewBox="0 0 10 10"><rect x="2.5" y="0.5" width="5" height="3"/><rect x="0.5" y="4" width="9" height="4.5" rx="1"/></symbol>
    <symbol id="icon-mail" viewBox="0 0 10 10"><path d="M0.5 2h9v6h-9z M0.5 2l4.5 3.5L9.5 2" /></symbol>
    <symbol id="icon-web" viewBox="0 0 10 10"><circle cx="5" cy="5" r="4.5"/></symbol>
  </svg>

  <section class="card" aria-label="Visitenkarte">
    <div class="brand"><span class="brand-dot"></span><span class="brand-name">TANNFELD</span></div>
    <div class="card-divider"></div>
    <div class="card-info">
      <div class="card-name">Carla Tannfeld</div>
      <div class="card-title">Dipl.-Wirtschaftsing. (FH)<br>Geschäftsführerin</div>
      <div class="card-address">Tannfeld Blechtechnik GmbH<br>Lindenweg 4<br>D-90210 Musterau. Deutschland</div>
      <ul class="contact-list">
        <li><svg><use href="#icon-phone"/></svg>+49 (0) 9100 55512-0</li>
        <li><svg><use href="#icon-mail"/></svg>c.tannfeld@tannfeld-gruppe.de</li>
        <li><svg><use href="#icon-web"/></svg>www.tannfeld-blt.de</li>
      </ul>
    </div>
  </section>

  <section class="letter" aria-label="Briefbogen">
    <div class="brand"><span class="brand-dot"></span><span class="brand-name">TANNFELD</span></div>
    <div class="sender-line">Tannfeld Blechtechnik GmbH, Lindenweg 4, D-90210 Musterau. Deutschland</div>
    <div class="letter-address">
      Tannfeld Blechtechnik GmbH<br>Lindenweg 4<br>D-90210 Musterau. Deutschland
      <ul class="contact-list">
        <li><svg><use href="#icon-phone"/></svg>+49 (0) 9100 55512-0</li>
        <li><svg><use href="#icon-fax"/></svg>+49 (0) 9100 55512-400</li>
        <li><svg><use href="#icon-mail"/></svg>c.tannfeld@tannfeld-gruppe.de</li>
        <li><svg><use href="#icon-web"/></svg>www.tannfeld-blt.de</li>
      </ul>
    </div>

    <div class="letter-body">
      <p class="salutation">Dear Mr. Hartmann,</p>
      <p class="text">Lorem ipsum dolor sit amet, consectetur adipiscing elit. Donec orci purus, luctus vitae dignissim eu, iaculis sed purus. Vivamus faucibus, ipsum nec aliquet viverra, leo mauris condimentum ligula, sit amet sagittis enim ligula quis arcu. Nam egestas tortor id nisi porttitor mattis. In tortor ante, ultricies in suscipit a, tempus non massa. Vivamus et auctor mi. Fusce vel massa nulla. Phasellus nec eros mauris, et scelerisque orci.</p>
      <p class="text">Donec malesuada orci vitae nulla accumsan porta a id massa. Quisque accumsan iaculis magna sit amet fringilla. Maecenas consequat, magna eget tincidunt semper, odio nibh rutrum mi, id feugiat ante nisi eu risus. Vestibulum nunc orci, rhoncus a placerat in, ultricies in mi. Cras mattis varius eros, vel fringilla nisi suscipit eget. Quisque scelerisque sagittis nulla at porttitor.</p>
      <p class="text">Sed id augue vitae urna euismod commodo aliquet a quam. Pellentesque arcu velit, cursus et malesuada ut, consequat et diam. Nullam erat sem, rhoncus id ullamcorper vitae, rhoncus et arcu. In ultricies ultricies nulla, ut rutrum nisi iaculis at. Donec eu magna a metus ornare faucibus. Fusce aliquet faucibus ultricies. Morbi semper, est id tincidunt gravida, sem arcu adipiscing lacus, ac bibendum nulla leo eu purus. Quisque nec diam sed risus consectetur a ccumsan quis quis nibh. Vestibulum id purus lorem.</p>
      <p class="text">It is a long established fact that a reader will be distracted by the readable content of a page when looking at its layout. The point of using Lorem Ipsum is that it has a more-or-less normal distribution of letters, as op&shy;posed to using 'Content here, content here', making it look like readable English. Many desktop publishing<br>packages</p>
      <p class="closing">Sincerely,</p>
      <div class="signature" role="img" aria-label="Handschriftliche Unterschrift"></div>
      <p class="signer">Paul Becker</p>
      <p class="signer-role">CEO/ Founder</p>
    </div>

    <div class="letter-footer">
      <div class="footer-col">Geschäftsführer<br>Georg Tannfeld<br>Carla Tannfeld<br>Werner Albrecht</div>
      <div class="footer-col">Registergericht Musterstadt<br>HRB: 10000. USt-IdNr. DE100000000<br>Steuer-Nr.:1000/100/10000</div>
      <div class="footer-col">Sparkasse Musterau<br>IBAN:DE00 1000 0000 0000 0000 01<br>BIC:MUSTDEX1XXX</div>
      <div class="footer-col">Handelsbank Musterstadt<br>IBAN : DE00 2000 0000 0000 0000 02<br>BIC : HANDDEX2XXX</div>
      <div class="footer-col">Handelsbank Musterstadt<br>IBAN : DE00 2000 0000 0000 0000 03<br>BIC : HANDDEX2XXX</div>
    </div>
    <div class="footer-note">Ein Unternehmen der Tannfeld Gruppe. www.tannfeld-gruppe.de</div>
  </section>

</div>
</body>
</html>
```